Business Card Design for Software Development Company

I am looking for a business card design the incorporates my new logo (attached below).

Key information to include:
Name: Darnell Whisket
Title: CEO
Email: darnell@brovatecore.com
Phone: 418-926-7301
Website: www.brovatecore.com

NOTE: This design should be easy to edit so that we can order cards for different members of our team.

```html
<!DOCTYPE html>
<html lang="en">
<head>
<meta charset="utf-8">
<title>BrovateLabs Business Card</title>
<link rel="stylesheet" href="https://fonts.googleapis.com/css2?family=Montserrat:wght@400;500;600;700&display=swap">
<style>
  :root {
    --navy: #333a52;
    --navy-card: #394157;
    --white: #ffffff;
    --teal: #1bb39a;
    --backdrop: #e6e7ea;
    --ink: #2b3147;
  }
  * { margin: 0; padding: 0; box-sizing: border-box; }
  html, body {
    width: 1200px;
    height: 1059px;
    overflow: hidden;
    background: var(--backdrop);
    font-family: "Montserrat", sans-serif;
  }
  .stage { position: relative; width: 1200px; height: 1059px; }
  .card {
    position: absolute;
    left: 255px;
    width: 690px;
    height: 392px;
    overflow: hidden;
    box-shadow: 0 8px 18px rgba(0,0,0,0.18);
  }
  .card--front { top: 100px; background: var(--white); }
  .card--back { top: 537px; background: var(--navy-card); }

  .brand { position: absolute; display: flex; flex-direction: column; align-items: flex-end; }
  .brand__row { display: flex; align-items: center; gap: 8px; }
  .brand__square { background: var(--teal); flex: none; }
  .brand__name { font-weight: 600; letter-spacing: -1px; line-height: 1; }
  .brand__tagline { font-weight: 600; text-transform: uppercase; letter-spacing: 0.4px; line-height: 1; }

  .card--front .brand { left: 29px; top: 66px; }
  .card--front .brand__square { width: 26px; height: 26px; }
  .card--front .brand__name { font-size: 54px; color: var(--navy); }
  .card--front .brand__tagline { font-size: 6.5px; color: var(--navy); margin-top: 3px; }

  .card--back .brand { left: 97px; top: 152px; }
  .card--back .brand__square { width: 36px; height: 36px; }
  .card--back .brand__name { font-size: 74px; color: var(--white); }
  .card--back .brand__tagline { font-size: 8.5px; color: var(--white); margin-top: 4px; }

  .person { position: absolute; left: 29px; top: 204px; color: var(--navy); }
  .person__name { font-size: 27px; font-weight: 700; text-transform: uppercase; letter-spacing: -0.2px; line-height: 1; }
  .person__title { font-size: 17px; font-weight: 400; margin-top: 4px; line-height: 1; }
  .person__rule { width: 24px; height: 1.5px; background: var(--navy); margin-top: 17px; }

  .contacts { position: absolute; left: 29px; top: 291px; list-style: none; color: var(--ink); }
  .contacts__item { display: flex; align-items: center; height: 26px; font-size: 16px; font-weight: 500; letter-spacing: 0.3px; }
  .contacts__icon { width: 13px; height: 13px; margin-right: 8px; fill: var(--navy); flex: none; }
</style>
</head>
<body>
<main class="stage">
  <section class="card card--front" aria-label="Card front">
    <div class="brand">
      <div class="brand__row">
        <span class="brand__square"></span>
        <span class="brand__name">BrovateLabs</span>
      </div>
      <span class="brand__tagline">A division of Brovate Core</span>
    </div>

    <div class="person">
      <h1 class="person__name">Darnell Whisket</h1>
      <p class="person__title">CEO</p>
      <div class="person__rule"></div>
    </div>

    <ul class="contacts">
      <li class="contacts__item">
        <svg class="contacts__icon" viewBox="0 0 16 16" aria-hidden="true"><path d="M3.6 1.2 5.8 3.8 4.5 5.6c.8 2.3 2.4 3.9 4.6 4.8l1.8-1.3 2.6 2.2-1.4 2.6C6.5 13.7 1.9 9 1.1 2.6z"/><path d="M9 1.5a6 6 0 0 1 5.5 5.5h-1.3A4.7 4.7 0 0 0 9 2.8zm0 2.6A3.4 3.4 0 0 1 11.9 7h-1.3A2.1 2.1 0 0 0 9 5.4z"/></svg>
        418-926-7301
      </li>
      <li class="contacts__item">
        <svg class="contacts__icon" viewBox="0 0 16 16" aria-hidden="true"><path d="M1 3h14v1.4L8 9 1 4.4z"/><path d="M1 6.1l7 4.6 7-4.6V13H1z"/></svg>
        darnell@brovatecore.com
      </li>
      <li class="contacts__item">
        <svg class="contacts__icon" viewBox="0 0 16 16" aria-hidden="true"><circle cx="8" cy="8" r="6.6" fill="none" stroke="currentColor" stroke-width="1.3" style="color:var(--navy)"/><ellipse cx="8" cy="8" rx="2.8" ry="6.6" fill="none" stroke="var(--navy)" stroke-width="1.1"/><path d="M1.5 6h13v1.1h-13zm0 3h13v1.1h-13z"/></svg>
        www.brovatecore.com
      </li>
    </ul>
  </section>

  <section class="card card--back" aria-label="Card back">
    <div class="brand">
      <div class="brand__row">
        <span class="brand__square"></span>
        <span class="brand__name">BrovateLabs</span>
      </div>
      <span class="brand__tagline">A division of Brovate Core</span>
    </div>
  </section>
</main>
</body>
</html>
```